Australian IT Company requires Business Card Design

Bluepeak is an Australian company that specialises in IT consulting & support, software development, project management, network services.

We have been in business for 15 years.

* We require a business card with the following on it:
Logo
Address
Contact Details
Space for staff name, title & mobile number

Industry/Entity Type

Software

```html
<!DOCTYPE html>
<html lang="en">
<head>
<meta charset="utf-8">
<title>Bluepeak Business Card</title>
<link rel="stylesheet" href="https://fonts.googleapis.com/css2?family=Open+Sans:wght@400;600;700&display=swap">
<style>
  :root {
    --page: #e9eaec;
    --card: #fbfbfc;
    --blue-deep: #33678f;
    --blue-mid: #4f86b0;
    --blue-soft: #7ea6c8;
    --lavender: #c5cbdc;
    --lavender-light: #dfe2ec;
    --grey-square: #7d7f82;
    --ink: #3c4150;
    --ink-soft: #5d6273;
    --line: #aab3c6;
  }
  * { margin: 0; padding: 0; box-sizing: border-box; }
  html, body { width: 1200px; height: 1000px; overflow: hidden; background: var(--page); }
  body { font-family: "Open Sans", Arial, sans-serif; position: relative; }

  .card {
    position: absolute; left: 150px; top: 230px;
    width: 900px; height: 540px;
    background: var(--card);
    box-shadow: 0 10px 30px rgba(0,0,0,.18);
    overflow: hidden;
  }

  .brand { position: absolute; left: 330px; top: 40px; display: flex; align-items: center; gap: 14px; }
  .brand-square { width: 46px; height: 46px; background: var(--blue-deep); }
  .brand-name { font-size: 44px; font-weight: 700; letter-spacing: 1px; color: var(--blue-deep); line-height: 1; }
  .brand-tagline { font-size: 11px; letter-spacing: 4px; text-transform: uppercase; color: var(--ink-soft); margin-top: 4px; white-space: nowrap; }

  .connector { position: absolute; width: 3px; background: var(--line); }
  .connector.one { left: 300px; top: 300px; height: 150px; }
  .connector.two { left: 560px; top: 260px; height: 120px; }

  .staff-box {
    position: absolute; left: 120px; top: 150px; width: 330px; height: 150px;
    background: linear-gradient(135deg, var(--blue-soft), var(--blue-mid));
    color: #fff; padding: 50px 26px 0;
  }
  .staff-name { font-size: 34px; font-weight: 700; line-height: 1.1; }
  .staff-position { font-size: 22px; line-height: 1.2; }

  .contact-box {
    position: absolute; left: 470px; top: 140px; width: 400px; height: 120px;
    background: linear-gradient(135deg, var(--lavender-light), var(--lavender));
    padding: 18px 24px; color: var(--ink);
  }
  .contact-line { display: flex; align-items: center; gap: 10px; font-size: 19px; line-height: 1.45; }
  .contact-line svg { width: 17px; height: 17px; flex: none; }

  .address-box {
    position: absolute; left: 470px; top: 330px; width: 330px; height: 140px;
    background: linear-gradient(135deg, #eceef4, var(--lavender-light));
    padding: 22px 24px; color: var(--ink-soft); font-size: 22px; line-height: 1.3;
  }

  .feature-band {
    position: absolute; left: 0; top: 300px; width: 330px; height: 240px;
    background: linear-gradient(160deg, var(--blue-deep), var(--blue-mid));
  }
  .corner-square { position: absolute; left: 340px; top: 470px; width: 60px; height: 60px; background: var(--grey-square); }
</style>
</head>
<body>
  <main class="card">
    <div class="brand">
      <div class="brand-square"></div>
      <div>
        <div class="brand-name">BLUEPEAK</div>
        <div class="brand-tagline">Smart technology, real support</div>
      </div>
    </div>

    <div class="connector one"></div>
    <div class="connector two"></div>

    <div class="feature-band"></div>
    <div class="corner-square"></div>

    <section class="staff-box">
      <div class="staff-name">Staff Name</div>
      <div class="staff-position">staff position</div>
    </section>

    <section class="contact-box">
      <div class="contact-line">
        <svg viewBox="0 0 24 24" aria-hidden="true"><path fill="#3c4150" d="M6.6 10.8a15 15 0 0 0 6.6 6.6l2.2-2.2a1 1 0 0 1 1-.25 11.4 11.4 0 0 0 3.6.57 1 1 0 0 1 1 1V20a1 1 0 0 1-1 1A17 17 0 0 1 3 4a1 1 0 0 1 1-1h3.5a1 1 0 0 1 1 1c0 1.25.2 2.45.57 3.57a1 1 0 0 1-.25 1z"/></svg>
        +61 3 9000 4821
      </div>
      <div class="contact-line">
        <svg viewBox="0 0 24 24" aria-hidden="true"><rect x="2" y="5" width="20" height="14" fill="#3c4150"/><path d="M2 5l10 8 10-8" fill="none" stroke="#dfe2ec" stroke-width="2"/></svg>
        staffname@bluepeak.net.au
      </div>
      <div class="contact-line">
        <svg viewBox="0 0 24 24" aria-hidden="true"><circle cx="12" cy="12" r="10" fill="#3c4150"/><path d="M2 12h20M12 2c3 3 3 17 0 20M12 2c-3 3-3 17 0 20" fill="none" stroke="#dfe2ec" stroke-width="1.5"/></svg>
        www.bluepeak.net.au
      </div>
    </section>

    <section class="address-box">
      <div>14 Ridge Road</div>
      <div>Tower Building 3</div>
      <div>Kingsbury Vic 3085</div>
    </section>
  </main>
</body>
</html>
```